Bottle label design for a mulberry brandy

Please create a label design for a mulberry brandy. The registered brand name is "Tavrik"
The brandy will be produced in Armenia from 100% mulberry.
Color of the product: transparent.
The product will be sold worldwide. The price will be between 30 and 50 USD. So the product will be in premium category.
Therefore we need a solid design, appropriate to the product price category. The design, however, needs to be modern and optimistic.
You can have mulberries on the label or not have, it is up to you.
We have chosen for the product some bottle types, the links to the available bottles you can find in the attachment. Ideally you show a picture of your label on the bottle you selected.

worldwide

```html
<!DOCTYPE html>
<html lang="en">
<head>
<meta charset="utf-8">
<title>Tavrik Mulberry Brandy – Label Variants</title>
<link href="https://fonts.googleapis.com/css2?family=Bodoni+Moda:wght@400;500&family=Montserrat:wght@400;600&display=swap" rel="stylesheet">
<style>
  :root {
    --paper: #ffffff;
    --glass-line: #e2e2e2;
    --red: #ff1f10;
    --plum: #5b0a43;
    --plum-deep: #4a0736;
    --berry-pink: #c24b8c;
    --gold: #a57a4c;
    --gold-soft: #d9c3a6;
    --ink-number: #5b0a43;
    --white: #ffffff;
  }
  * { margin: 0; padding: 0; box-sizing: border-box; }
  html, body {
    width: 1200px; height: 597px; overflow: hidden;
    background: var(--paper);
  }
  .sheet { position: relative; width: 1200px; height: 597px; }

  .variant { position: absolute; top: 0; width: 206px; height: 597px; }
  .variant--red     { left: 132px; }
  .variant--pattern { left: 521px; }
  .variant--panel   { left: 896px; }

  /* neck wrap */
  .neck {
    position: absolute; left: 62px; top: 30px; width: 82px; height: 148px;
    border-radius: 4px 4px 2px 2px; overflow: hidden;
  }
  .neck--red { background: var(--red); }
  .neck--pattern { background: linear-gradient(160deg, var(--berry-pink) 0%, var(--plum) 45%, var(--berry-pink) 75%, var(--plum) 100%); }
  .neck--plum { background: var(--plum); }
  .neck__rule {
    position: absolute; left: 4px; right: 4px; top: 38px; height: 1.5px; background: var(--gold);
  }
  .neck__name {
    position: absolute; left: 50%; top: 92px;
    transform: translate(-50%, -50%) rotate(-90deg);
    font-family: "Bodoni Moda", serif; font-weight: 400; font-size: 22px;
    line-height: 1; color: var(--white); letter-spacing: 0.3px; white-space: nowrap;
  }

  /* front label area */
  .front {
    position: absolute; left: 0; top: 196px; width: 206px; height: 360px;
    border: 1px solid var(--glass-line); border-radius: 6px;
  }
  .front__kicker {
    position: absolute; top: 30px; width: 100%; text-align: center;
    font-family: "Montserrat", sans-serif; font-weight: 600; font-size: 7.5px;
    letter-spacing: 2.4px; color: var(--gold);
  }
  .front__origin {
    position: absolute; top: 43px; width: 100%; text-align: center;
    font-family: "Montserrat", sans-serif; font-size: 7px; color: var(--red);
  }
  .front__name {
    position: absolute; top: 150px; width: 100%; text-align: center;
    font-family: "Bodoni Moda", serif; font-weight: 400; font-size: 31px;
    letter-spacing: 0.5px; color: var(--gold); line-height: 1;
  }
  .band {
    position: absolute; left: 0; right: 0; top: 193px; height: 159px;
    border-top: 1px solid var(--gold);
  }
  .band__art { position: absolute; inset: 0; }
  .band__art--line { background: linear-gradient(180deg, rgba(217,195,166,0.35), rgba(217,195,166,0.15)); }
  .band__art--pattern { background: linear-gradient(135deg, var(--plum) 0%, var(--berry-pink) 35%, var(--plum) 55%, var(--berry-pink) 80%, var(--plum) 100%); }
  .band__art--panel { left: 26px; right: 24px; background: linear-gradient(180deg, #6e1a55, var(--plum)); }
  .band__stripe {
    position: absolute; left: 0; right: 0; top: 42px; height: 42px; background: var(--red);
  }
  .band__product {
    position: absolute; top: 56px; width: 100%; text-align: center;
    font-family: "Montserrat", sans-serif; font-size: 8px; letter-spacing: 2.2px;
    color: var(--white);
  }
  .band__made {
    position: absolute; top: 69px; width: 100%; text-align: center;
    font-family: "Montserrat", sans-serif; font-size: 4.5px; color: var(--white);
  }
  .band__volume {
    position: absolute; top: 137px; width: 100%; text-align: center;
    font-family: "Montserrat", sans-serif; font-size: 7px; color: var(--plum);
  }
  .variant--pattern .band__volume,
  .variant--panel .band__volume { color: var(--white); }

  .plum-panel {
    position: absolute; left: 26px; width: 156px; top: 20px; height: 332px;
    background: var(--plum);
  }
  .variant--panel .front__origin { color: var(--white); }

  .variant__number {
    position: absolute; top: 530px; left: 250px;
    font-family: "Bodoni Moda", serif; font-size: 34px; color: var(--ink-number); line-height: 1;
  }
</style>
</head>
<body>
<main class="sheet">

  <section class="variant variant--red">
    <div class="neck neck--red">
      <div class="neck__rule"></div>
      <span class="neck__name">TAVRIK</span>
    </div>
    <div class="front">
      <p class="front__kicker">PREMIUM QUALITY</p>
      <p class="front__origin">100% mulberry</p>
      <p class="front__name">TAVRIK</p>
      <div class="band">
        <div class="band__art band__art--line" role="img" aria-label="Gold line illustration of mulberries and leaves"></div>
        <div class="band__stripe"></div>
        <p class="band__product">MULBERRY BRANDY</p>
        <p class="band__made">product of Armenia</p>
        <p class="band__volume">Vol%40 500ml</p>
      </div>
    </div>
    <span class="variant__number">1</span>
  </section>

  <section class="variant variant--pattern">
    <div class="neck neck--pattern" role="img" aria-label="Plum and pink mulberry pattern">
      <div class="neck__rule"></div>
      <span class="neck__name">TAVRIK</span>
    </div>
    <div class="front">
      <p class="front__kicker">PREMIUM QUALITY</p>
      <p class="front__origin">100% mulberry</p>
      <p class="front__name">TAVRIK</p>
      <div class="band">
        <div class="band__art band__art--pattern" role="img" aria-label="Plum and pink pattern with gold mulberries and leaves"></div>
        <p class="band__product">MULBERRY BRANDY</p>
        <p class="band__made">product of Armenia</p>
        <p class="band__volume">Vol%40 500ml</p>
      </div>
    </div>
    <span class="variant__number">2</span>
  </section>

  <section class="variant variant--panel">
    <div class="neck neck--plum">
      <div class="neck__rule"></div>
      <span class="neck__name">TAVRIK</span>
    </div>
    <div class="front">
      <div class="plum-panel"></div>
      <p class="front__origin">100% mulberry</p>
      <p class="front__name">TAVRIK</p>
      <div class="band">
        <div class="band__art band__art--panel" role="img" aria-label="Gold line illustration of mulberries and leaves on plum"></div>
        <p class="band__product">MULBERRY BRANDY</p>
        <p class="band__made">product of Armenia</p>
        <p class="band__volume">Vol%40 500ml</p>
      </div>
    </div>
    <span class="variant__number">3</span>
  </section>

</main>
</body>
</html>
```